Brochure Design Project

We need a brochure design, copy writing and print ready art for a Toronto based commercial cleaning company. Output should be an 8.5X11 four page piece.

We provide "green cleaning" - environmentally friendly cleaning programs. Our positioning is strongly environmentally oriented, high quality, reliable and affordable.

We provide interior cleaning for office buildings, condominiums, manufacturing facilities, gyms, retail stores, daycares, churches and banquet facilities.

Core services are; regularly scheduled cleaning programs, floor maintenance, carpet cleaning, window cleaning, construction cleaning and sanitary supply management.

Looking for a "fresh" clean look that screams "competent" and "professional" and clearly communicates "affordability"

The piece will be used as a stand alone mailer and leave behind for a salesperson.

Reason: Designs have not met the brief specifications

Target Market(s)

Mid level managers of virtually every "non food service" company, facility or operation. Slightly skewed to female decision makers

Industry/Entity Type

Construction

Requirements
Must have
• Clear identification of the key services with image support, ie floor maintenance image, carpet cleaning

```html
<!DOCTYPE html>
<html lang="en">
<head>
<meta charset="utf-8">
<title>Clearwell Services – Brochure Spread</title>
<link href="https://fonts.googleapis.com/css2?family=Luckiest+Guy&family=Comfortaa:wght@300;400;600&display=swap" rel="stylesheet">
<style>
  :root{
    --backdrop:#e9eaec;
    --page-blue:#5aaee0;
    --deep-blue:#234a9b;
    --tile-light:#8cc6ec;
    --ink-navy:#1d3c8c;
    --leaf-green:#7cb940;
    --paper:#ffffff;
    --ink-black:#111111;
    --rule:#2f6fb6;
  }
  *{box-sizing:border-box;margin:0;padding:0}
  html,body{width:1200px;height:900px;overflow:hidden;background:var(--backdrop)}
  body{font-family:"Comfortaa",sans-serif;color:var(--paper);position:relative}

  .spread{position:absolute;left:60px;top:100px;width:1080px;height:700px;display:flex;
    box-shadow:0 18px 40px rgba(0,0,0,.18)}
  .page{position:relative;width:540px;height:700px;background:var(--page-blue);overflow:hidden}
  .page--left{border-right:1px solid rgba(0,0,0,.08)}

  .section-title{position:absolute;font-family:"Luckiest Guy",sans-serif;font-size:27px;letter-spacing:.5px;line-height:1;padding:6px 0 0 18px;height:34px;isolation:isolate;white-space:nowrap}
  .section-title::before{content:"";position:absolute;left:0;right:-60px;top:10px;height:22px;background:var(--paper);border-radius:0 20px 20px 0;z-index:-1}
  .section-title span{position:relative}
  .title--services{left:0;top:22px;width:300px;color:var(--ink-navy)}
  .title--green{left:20px;top:22px;width:540px;color:var(--leaf-green)}
  .title--green::before{border-radius:20px}
  .title--pricing{left:20px;top:312px;width:540px;color:var(--ink-black)}
  .title--pricing::before{border-radius:20px}

  .body-copy{position:absolute;font-size:9.5px;line-height:13px;font-weight:300}
  .services-intro{left:30px;top:66px;width:480px}

  .experience-banner{position:absolute;left:30px;top:138px;width:480px;height:88px;background:var(--deep-blue);
    border-radius:22px 22px 40px 22px;padding:17px 22px;font-size:10px;line-height:19px;text-transform:uppercase;white-space:nowrap}

  .service-grid{position:absolute;left:30px;top:250px;width:480px;display:grid;grid-template-columns:repeat(3,140px);column-gap:30px;row-gap:26px}
  .service{display:flex;flex-direction:column}
  .service__label{font-size:9.5px;line-height:12px;text-transform:uppercase;height:28px;display:flex;align-items:flex-end;padding-bottom:5px}
  .service__tile{width:140px;height:140px;background:var(--deep-blue);border-radius:18px;display:flex;align-items:center;justify-content:center;
    box-shadow:0 0 0 2px rgba(255,255,255,.25)}
  .service__tile svg{width:104px;height:104px}

  .green-intro{left:30px;top:64px;width:480px}
  .benefits{position:absolute;left:20px;top:118px;width:500px;height:182px;background:var(--leaf-green);border-radius:24px;
    padding:16px 24px;list-style:none;font-size:11px;line-height:19.5px;text-transform:uppercase;letter-spacing:.2px;white-space:nowrap}

  .pricing-intro{left:30px;top:354px;width:480px}
  .price-table{position:absolute;left:30px;top:414px;width:480px;border-collapse:collapse;background:var(--paper);color:var(--rule);font-size:10.5px}
  .price-table td{border:1px solid var(--rule);height:21px;padding:0 8px}
  .price-table .row-head{text-transform:uppercase}
  .price-table .row-sub{font-size:9.5px;padding-left:18px}
  .price-table .row-strong{color:var(--ink-black);text-transform:uppercase}
  .price-table .price{width:130px;white-space:nowrap}
  .price-table .price--event{color:var(--ink-black)}

  .sub-title{position:absolute;left:30px;font-size:11.5px;font-weight:600;text-transform:uppercase;color:var(--ink-black)}
  .guarantee-title{top:518px}
  .guarantee-copy{left:30px;top:534px;width:480px}
  .keen-title{top:636px}
  .keen-copy{left:30px;top:652px;width:480px}
</style>
</head>
<body>
<main class="spread">
  <section class="page page--left">
    <h2 class="section-title title--services"><span>OUR SERVICES</span></h2>
    <p class="body-copy services-intro">Clearwell Services will deliver a professional, environmentally friendly, effective, efficient and affordable maintenance program. We are confident that we can deliver a program that will help you achieve your goal to improve your site's presentation, staff comfort and appearance for your customers while remaining cost effective. Earning your business today is very important to us; earning it every day is our mission.</p>
    <div class="experience-banner">
      Over 25 years of facilities management experience<br>
      Integrity and reliability with a quality service ethic<br>
      Passion for excellence and desire to improve our way of life
    </div>

    <div class="service-grid">
      <div class="service">
        <div class="service__label">Regularly scheduled cleaning programs</div>
        <div class="service__tile">
          <svg viewBox="0 0 104 104" aria-hidden="true">
            <rect x="10" y="12" width="84" height="84" rx="6" fill="#fff"/>
            <rect x="10" y="12" width="84" height="22" rx="6" fill="#8cc6ec"/>
            <text x="52" y="55" text-anchor="middle" font-family="Comfortaa, sans-serif" font-size="15" fill="#5aaee0">october</text>
            <text x="52" y="88" text-anchor="middle" font-family="Comfortaa, sans-serif" font-weight="600" font-size="34" fill="#5aaee0">2</text>
          </svg>
        </div>
      </div>
      <div class="service">
        <div class="service__label">Floor maintenance</div>
        <div class="service__tile">
          <svg viewBox="0 0 104 104" aria-hidden="true">
            <rect x="8" y="8" width="88" height="88" fill="#fff"/>
            <g fill="#8cc6ec">
              <rect x="12" y="12" width="25" height="25"/><rect x="40" y="12" width="25" height="25"/><rect x="68" y="12" width="24" height="25"/>
              <rect x="12" y="40" width="25" height="25"/><rect x="40" y="40" width="25" height="25"/><rect x="68" y="40" width="24" height="25"/>
              <rect x="12" y="68" width="25" height="24"/><rect x="40" y="68" width="25" height="24"/><rect x="68" y="68" width="24" height="24"/>
            </g>
          </svg>
        </div>
      </div>
      <div class="service">
        <div class="service__label">Carpet cleaning</div>
        <div class="service__tile">
          <svg viewBox="0 0 104 104" role="img" aria-label="Carpet texture square">
            <rect x="8" y="8" width="88" height="88" fill="#fff"/>
            <rect x="12" y="12" width="80" height="80" fill="#8cc6ec"/>
          </svg>
        </div>
      </div>
      <div class="service">
        <div class="service__label">Window cleaning</div>
        <div class="service__tile">
          <svg viewBox="0 0 104 104" aria-hidden="true">
            <rect x="14" y="10" width="76" height="84" fill="#fff"/>
            <rect x="19" y="15" width="31" height="36" fill="#8cc6ec"/><rect x="54" y="15" width="31" height="36" fill="#8cc6ec"/>
            <rect x="19" y="55" width="31" height="34" fill="#8cc6ec"/><rect x="54" y="55" width="31" height="34" fill="#8cc6ec"/>
          </svg>
        </div>
      </div>
      <div class="service">
        <div class="service__label">Construction cleaning</div>
        <div class="service__tile">
          <svg viewBox="0 0 104 104" aria-hidden="true">
            <path d="M22 70 A32 32 0 0 1 82 70 Z" fill="#8cc6ec" stroke="#fff" stroke-width="3"/>
            <path d="M10 72 H94 Q94 80 86 80 H18 Q10 80 10 72 Z" fill="#fff"/>
          </svg>
        </div>
      </div>
      <div class="service">
        <div class="service__label">Sanitary supply management</div>
        <div class="service__tile">
          <svg viewBox="0 0 104 104" aria-hidden="true">
            <circle cx="52" cy="52" r="40" fill="#fff"/>
            <circle cx="52" cy="52" r="14" fill="#8cc6ec"/>
          </svg>
        </div>
      </div>
    </div>
  </section>

  <section class="page page--right">
    <h2 class="section-title title--green"><span>GREEN CLEANING PROGRAM</span></h2>
    <p class="body-copy green-intro">Green cleaning refers to using cleaning methods and products with environmentally-friendly ingredients to preserve human health and environmental quality. Green cleaning techniques and products avoid the use of chemically-reactive and toxic cleaning products which contain various toxic chemicals, some of which emit volatile organic compounds into the air.</p>
    <ul class="benefits">
      <li>Improved indoor air quality</li>
      <li>Fewer complaints from staff about their indoor environment</li>
      <li>Reduced or no adverse environmental impact</li>
      <li>Saving company owners money</li>
      <li>Conserving natural resources</li>
      <li>Enhancing and protecting natural habitats</li>
      <li>Improving employee productivity and satisfaction</li>
      <li>Optimizing life-cycle performance of building materials</li>
    </ul>

    <h2 class="section-title title--pricing"><span>PRICING &amp; GUARANTEE</span></h2>
    <p class="body-copy pricing-intro">Clearwell Services will furnish all labor, supervision, cleaning products and equipment, excluding customer consumed sanitary products and supplies, to provide a thorough green cleaning program and maintain the areas outlined in the cleaning specification. All work will be professionally performed with quality workmanship.</p>
    <table class="price-table">
      <tr><td class="row-head">Monthly maintenance (MM)</td><td class="price"></td></tr>
      <tr><td class="row-sub">2X per week cycle</td><td class="price">$ 897 per month</td></tr>
      <tr><td class="row-sub">3X per week cycle</td><td class="price">$ 1334 per month</td></tr>
      <tr><td class="row-strong">Semi annual maintenance (SAM)</td><td class="price price--event">$ 1940 per event</td></tr>
    </table>

    <h3 class="sub-title guarantee-title">Our guarantee</h3>
    <p class="body-copy guarantee-copy">We commit to 100% satisfaction. Should any of our cleaning tasks fall short of your expectations, we will promptly return and repeat the task until you are completely satisfied. Our goal is to provide the best service available. Professionalism and reliability you can count on. Our cleaners have been carefully selected and properly trained to understand and deliver high quality green cleaning programs. Before joining Clearwell Services our staff have submitted to background checks to help ensure the integrity of our team. In addition we conduct monthly inspections to ensure the quality of our program.</p>
    <h3 class="sub-title keen-title">Keen to clean</h3>
    <p class="body-copy keen-copy">We can finalize your custom specifications, train staff, put equipment in place and begin your program within 2 weeks of receiving your approval.</p>
  </section>
</main>
</body>
</html>
```